Packaging label for launch of sun dried tomato products.

Established family farm in South Africa growing fruit for the production of dried fruit. We need a packaging label for the launch of our sun dried tomato products ie dried tomatoes in olive oil, dried tomato flakes and tomato powder. Packaging will be a round glass "jam jar" and spice shaker bottle. Due to limited amount of product available we cannot market to the masses, but rather focus on conveying a message of quality and exclusivity.

Target Market(s)

Home chef

Industry/Entity Type

Food

Font styles to use
Serif

Requirements
Nice to have
• Include the farm name in the design. TAVSONE

```html
<!DOCTYPE html>
<html lang="en">
<head>
<meta charset="utf-8">
<title>Tavsone Sun-Dried Tomatoes Label</title>
<link rel="stylesheet" href="https://fonts.googleapis.com/css2?family=Bebas+Neue&family=IM+Fell+English+SC&family=Libre+Caslon+Text&display=swap">
<style>
  :root {
    --backdrop: #3f3f3f;
    --label-black: #0b0b0b;
    --tomato-red: #b30d0d;
    --paper-white: #f4f2ee;
    --hatch-white: rgba(244, 242, 238, 0.55);
    --hatch-red: rgba(179, 13, 13, 0.6);
  }
  html, body {
    margin: 0;
    width: 1200px;
    height: 738px;
    overflow: hidden;
    background: var(--backdrop);
  }
  .label {
    position: absolute;
    left: 198px;
    top: 40px;
    width: 803px;
    height: 659px;
    background: var(--label-black);
    color: var(--paper-white);
  }
  .rule {
    position: absolute;
    height: 13px;
    background: var(--tomato-red);
  }
  .rule--top-left { left: 0; top: 59px; width: 247px; }
  .rule--top-right { left: 556px; top: 59px; right: 0; }
  .rule--bottom-left { left: 0; top: 611px; width: 349px; height: 6px; }
  .rule--bottom-right { left: 456px; top: 611px; right: 0; height: 6px; }

  .brand {
    position: absolute;
    left: 0; right: 0;
    top: 28px;
    margin: 0;
    text-align: center;
    font-family: "IM Fell English SC", serif;
    font-weight: 400;
    font-size: 56px;
    line-height: 1;
    letter-spacing: 1px;
    color: var(--paper-white);
  }
  .title {
    position: absolute;
    left: 0; right: 0;
    text-align: center;
    font-family: "Bebas Neue", sans-serif;
    line-height: 1;
  }
  .title--sun-dried {
    top: 124px;
    font-size: 130px;
    letter-spacing: 2px;
    color: var(--paper-white);
    text-shadow: 3px 3px 0 var(--label-black), 5px 5px 0 var(--hatch-white);
  }
  .title--tomatoes {
    top: 224px;
    font-size: 204px;
    letter-spacing: 1px;
    color: var(--tomato-red);
    text-shadow: 4px 4px 0 var(--label-black), 7px 7px 0 var(--hatch-red);
  }
  .subtitle {
    position: absolute;
    left: 0; right: 0;
    top: 390px;
    text-align: center;
    font-family: "Libre Caslon Text", serif;
    font-size: 36px;
    line-height: 1;
    letter-spacing: 9px;
    color: var(--paper-white);
  }
  .subtitle-dash {
    position: absolute;
    top: 410px;
    height: 3px;
    background: var(--paper-white);
    border-radius: 2px;
  }
  .subtitle-dash--left { left: 113px; width: 104px; }
  .subtitle-dash--right { left: 585px; width: 107px; }

  .product-photo {
    position: absolute;
    z-index: 1;
    left: 492px;
    top: 462px;
    width: 178px;
    height: 112px;
    border-radius: 45% 55% 50% 50% / 55% 45% 55% 45%;
    background: radial-gradient(ellipse at 60% 50%, #c2361c 0%, #8e1a10 55%, #4a0c07 100%);
  }
  .features {
    position: absolute;
    z-index: 2;
    left: 134px;
    top: 468px;
    width: 421px;
    height: 96px;
    border: 2px solid var(--paper-white);
    box-sizing: border-box;
    margin: 0;
    padding: 0;
    list-style: none;
  }
  .features li {
    height: 31px;
    box-sizing: border-box;
    padding-left: 10px;
    display: flex;
    align-items: center;
    white-space: nowrap;
    font-family: "Libre Caslon Text", serif;
    font-size: 9px;
    text-transform: uppercase;
    color: var(--paper-white);
  }
  .features li + li { border-top: 2px solid var(--paper-white); }

  .net-weight {
    position: absolute;
    left: 0; right: 0;
    top: 595px;
    text-align: center;
    font-family: "Bebas Neue", sans-serif;
    font-size: 38px;
    line-height: 1;
    color: var(--paper-white);
  }
</style>
</head>
<body>
  <main class="label">
    <div class="rule rule--top-left"></div>
    <div class="rule rule--top-right"></div>
    <h1 class="brand">TAVSONE</h1>

    <div class="title title--sun-dried">SUN-DRIED</div>
    <div class="title title--tomatoes">TOMATOES</div>

    <div class="subtitle-dash subtitle-dash--left"></div>
    <div class="subtitle">IN OLIVE OIL</div>
    <div class="subtitle-dash subtitle-dash--right"></div>

    <div class="product-photo" role="img" aria-label="Photograph of sun-dried tomato halves"></div>
    <ul class="features">
      <li>Lorem ipsum dolor sit amet, consectetur adipiscing elit</li>
      <li>Lorem ipsum dolor sit amet, consectetur adipiscing</li>
      <li>Lorem ipsum dolor sit amet, consectetur adipiscing</li>
    </ul>

    <div class="rule rule--bottom-left"></div>
    <div class="net-weight">200GMS</div>
    <div class="rule rule--bottom-right"></div>
  </main>
</body>
</html>
```